Banners for a bowtie/tie Fashion shop

I need banners (770x100) for a necktie and bowtie shop (http://www.movelia.dk)

5 BOWTIE BANNERS:

I need the 3 text versions for eatch bowtie banner:

Danmarks største udvalg af butterfly
Køb butterfly. FRI fragt og FRI retur
Butterfly fra 199,- inkl. FRI fragt

5 NECKTIE BANNERS:

I need the 3 text versions for eatch necktie banner:

Danmarks største udvalg af slips
Køb slips. FRI fragt og FRI retur
Slips fra 199,- inkl. FRI fragt

All banners should contain the logo. All in JPG format and Photoshop/Inddesign/illustrator format

Target Market(s)

Guys and Gays

Industry/Entity Type

Shop

Requirements
Must have
• Logo
Nice to have
• Nice new pictures

```html
<!DOCTYPE html>
<html lang="da">
<head>
<meta charset="utf-8">
<title>Knotwell – Danmarks største udvalg af slips</title>
<link rel="stylesheet" href="https://fonts.googleapis.com/css2?family=Passion+One&family=Pacifico&display=swap">
<style>
  :root {
    --ink: #111418;
    --accent: #6fb8d2;
    --accent-dark: #1d2a33;
    --sky-light: #f4f6f6;
    --sky-mid: #e3e8ea;
    --suit: #5fa6c4;
    --suit-deep: #3d7f9f;
    --name: #ffffff;
  }
  html, body {
    margin: 0;
    padding: 0;
    width: 1200px;
    height: 156px;
    overflow: hidden;
    background: var(--sky-light);
  }
  .banner {
    position: relative;
    width: 1200px;
    height: 156px;
    overflow: hidden;
  }
  .banner__scene {
    position: absolute;
    inset: 0;
    background:
      linear-gradient(90deg,
        var(--sky-light) 0%,
        var(--sky-mid) 35%,
        #d9e0e2 60%,
        #c9d6da 70%,
        var(--suit) 79%,
        var(--suit-deep) 90%,
        #a9c7d2 100%);
  }
  .banner__headline {
    position: absolute;
    left: 15px;
    top: 38px;
    margin: 0;
    display: flex;
    align-items: baseline;
    gap: 8px;
    white-space: nowrap;
  }
  .banner__lead {
    font-family: "Passion One", sans-serif;
    font-weight: 400;
    font-size: 50px;
    letter-spacing: 0;
    color: var(--ink);
    line-height: 1;
  }
  .banner__product {
    font-family: "Pacifico", cursive;
    font-size: 54px;
    color: var(--accent);
    -webkit-text-stroke: 1.5px var(--accent-dark);
    line-height: 1;
  }
  .banner__brand {
    position: absolute;
    right: 28px;
    bottom: 12px;
    display: flex;
    align-items: center;
    gap: 7px;
    font-family: "Passion One", sans-serif;
    font-size: 22px;
    letter-spacing: 1px;
    color: var(--name);
    text-transform: uppercase;
    text-decoration: none;
    line-height: 1;
  }
  .banner__brand-mark {
    width: 9px;
    height: 9px;
    background: var(--name);
  }
</style>
</head>
<body>
  <div class="banner">
    <div class="banner__scene" role="img" aria-label="Soft city skyline with a clock tower and a man in a light blue suit and dark tie"></div>
    <h1 class="banner__headline">
      <span class="banner__lead">DANMARKS STØRSTE UDVALG AF</span>
      <span class="banner__product">slips</span>
    </h1>
    <a class="banner__brand" href="http://www.knotwell.dk"><span class="banner__brand-mark"></span>Knotwell</a>
  </div>
</body>
</html>
```